Need a Hollin & Co
* logo
* word and powerpoint livery
* basic webpage

Hollin & Co is a Private M&A Advisor. We want to look like http://www.vantrelcapital.example
It needs to communicate reliabity, conservativeness and discretion.

```html
<!DOCTYPE html>
<html lang="en">
<head>
<meta charset="utf-8">
<title>Hollin &amp; Co — Private M&amp;A Advisory</title>
<link href="https://fonts.googleapis.com/css2?family=Gelasio:wght@400;700&display=swap" rel="stylesheet">
<style>
:root{
  --navy:#15356b;
  --blue:#2b5d9a;
  --blue-deep:#1a3f78;
  --sky:#3f9fd6;
  --ink:#222;
  --text:#333;
  --footer:#2d2d2d;
  --white:#fff;
}
*{margin:0;padding:0;box-sizing:border-box}
html,body{width:837px;height:1200px;overflow:hidden}
body{position:relative;font-family:"Gelasio",Georgia,serif;color:var(--text);background:var(--white)}
.abs{position:absolute}

.site-header{left:0;top:0;width:837px;height:62px;background:linear-gradient(#fafafa,#e9e9e9);box-shadow:0 2px 4px rgba(0,0,0,.25);z-index:2}
.brand{left:133px;top:26px;font-size:21px;font-weight:400;color:var(--ink);letter-spacing:.2px}
.main-nav{left:342px;top:20px;width:363px;height:42px;border-radius:6px 6px 0 0;background:linear-gradient(#3f78b4,#23528f);display:flex;overflow:hidden}
.main-nav a{color:var(--white);text-decoration:none;font-size:10px;line-height:42px;text-align:center;white-space:nowrap;flex:none}
.main-nav a.active{background:linear-gradient(#55b5e6,#3298d2)}

.hero{left:0;top:62px;width:837px;height:319px;background:linear-gradient(#4f7db3,#2b5d9a 55%,#1d4785)}
.slide{left:133px;top:90px;width:572px;height:255px;background:linear-gradient(115deg,#123c7a 0%,#1d6ed0 45%,#1a4f9a 70%,#c9ced6 100%);box-shadow:0 14px 14px -6px rgba(0,0,0,.55)}
.caption{background:rgba(20,20,20,.82);color:var(--white);font-size:11px;padding:0 8px;height:33px;line-height:33px}
.dots{left:389px;top:320px;display:flex;gap:5px}
.dots span{width:8px;height:8px;border-radius:50%;background:var(--white)}
.dots span.on{background:#46c0d8}

.about{left:0;top:381px;width:837px;height:276px;background:linear-gradient(#f2f2f2,#e2e2e2)}
.section-title{font-size:11px;font-weight:700;color:var(--ink);letter-spacing:.2px}
.value{width:177px;height:220px;top:437px;color:var(--white);text-align:center}
.value svg.shape{position:absolute;left:0;top:0}
.value .icon{position:absolute;left:0;top:40px;width:177px;display:flex;justify-content:center}
.value h3{position:absolute;width:177px;font-size:11.5px;font-weight:700}
.value p{position:absolute;left:12px;width:153px;font-size:8.3px;line-height:14.4px}

.heading{top:689px;font-size:11px;font-weight:700;color:var(--ink)}
.pager{top:688px;width:19px;height:14px;background:var(--blue-deep);display:flex;align-items:center;justify-content:center}
.photo{background:linear-gradient(100deg,#e9eef2,#b9c8d8 40%,#2a4a7a 75%,#d9e2ea)}
.body-copy{left:131px;width:305px;font-size:8.4px;line-height:14.4px;color:var(--text)}
.news-img{left:452px;width:252px;height:96px}
.news-a{background:linear-gradient(120deg,#f2f2f2,#d8dde0 45%,#bfd36a 75%,#eef0ea)}
.news-b{background:linear-gradient(120deg,#1c2b40,#3d5a78 50%,#5f8fb0 75%,#22384f)}
.date{left:452px;width:49px;height:44px;background:var(--blue);color:var(--white);text-align:center;font-weight:700;font-size:13px;line-height:13px;padding-top:9px}
.date small{display:block;font-weight:400;font-size:12px}
.news-text{left:510px;width:195px;font-size:8.3px;line-height:14.4px;color:var(--text)}

.partners{left:0;top:1058px;width:837px;height:82px;background:linear-gradient(#f4f4f4,#e4e4e4);display:flex;align-items:center;justify-content:space-between;padding:0 138px}
.partner{font-size:14px;font-weight:400;color:#3a3a3a;display:flex;align-items:center;gap:5px}
.partner i{width:10px;height:10px;background:#8a8a8a;display:block}

.site-footer{left:0;top:1140px;width:837px;height:60px;background:var(--footer);color:var(--white)}
.foot-nav{left:133px;top:14px;font-size:8.5px;display:flex}
.foot-nav span{padding:0 12px}
.foot-nav span:first-child{padding-left:0}
.foot-nav b{font-weight:400}
.copyright{left:133px;top:34px;font-size:8.5px}
.social{left:646px;top:18px;display:flex;gap:3px}
.social span{width:19px;height:19px;border:1.3px solid #ddd;border-radius:50%}
</style>
</head>
<body>

<header class="site-header abs">
  <div class="brand abs">Hollin &amp; Co</div>
  <nav class="main-nav abs">
    <a class="active" href="#" style="width:68px">Home</a><a href="#" style="width:44px">About</a><a href="#" style="width:68px">Services</a><a href="#" style="width:40px">Press</a><a href="#" style="width:64px">Career</a><a href="#" style="width:79px">Contact Us</a>
  </nav>
</header>

<section class="hero abs"></section>
<div class="slide abs" role="img" aria-label="Financial market chart on a screen with a pen pointing at it"></div>
<div class="caption abs" style="left:141px;top:228px">Neque porro quisquam est qui dolorem ipsum quia dolor</div>
<div class="caption abs" style="left:141px;top:267px">Sit amet, consectetur, adipisci velit...</div>
<div class="dots abs"><span class="on"></span><span></span><span></span><span></span><span></span></div>

<section class="about abs"></section>
<h2 class="section-title abs" style="left:375px;top:397px">WHO WE ARE ?</h2>

<div class="value abs" style="left:133px">
  <svg class="shape" width="177" height="220"><defs><linearGradient id="g1" x1="0" y1="0" x2="0" y2="1"><stop offset="0" stop-color="#4e82bd"/><stop offset="1" stop-color="#15356b"/></linearGradient></defs><path d="M0 29 L88.5 0 L177 29 V220 H0Z" fill="url(#g1)"/></svg>
  <div class="icon"><svg width="26" height="42" viewBox="0 0 26 42"><path d="M5 18 V11 a8 8 0 0 1 16 0 V18" fill="none" stroke="#fff" stroke-width="4"/><path d="M0 18 H26 V31 Q26 38 13 42 Q0 38 0 31Z" fill="#fff"/><circle cx="13" cy="27" r="2.6" fill="#2b5d9a"/><rect x="12" y="27" width="2" height="6" fill="#2b5d9a"/></svg></div>
  <h3 style="top:97px">Secretive</h3>
  <p style="top:120px">Lorem Ipsum is simply dummy text of the printing and typesetting industry. Lorem Ipsum has been the industry's standard dummy text ever since the 1500s, when an unknown printer</p>
</div>
<div class="value abs" style="left:330px">
  <svg class="shape" width="177" height="220"><path d="M0 29 L88.5 0 L177 29 V220 H0Z" fill="url(#g1)"/></svg>
  <div class="icon" style="top:50px"><svg width="48" height="26" viewBox="0 0 48 26"><path d="M0 26 A24 24 0 0 1 48 26Z" fill="#fff"/><path d="M24 24 L36 10" stroke="#2b5d9a" stroke-width="3"/><circle cx="24" cy="24" r="3" fill="#2b5d9a"/></svg></div>
  <h3 style="top:93px">Reliable</h3>
  <p style="top:120px">Lorem Ipsum is simply dummy text of the printing and typesetting industry. Lorem Ipsum has been the industry's standard dummy text ever since the 1500s, when an unknown printer</p>
</div>
<div class="value abs" style="left:528px">
  <svg class="shape" width="177" height="220"><path d="M0 29 L88.5 0 L177 29 V220 H0Z" fill="url(#g1)"/></svg>
  <div class="icon" style="top:44px"><svg width="40" height="36" viewBox="0 0 40 36"><path d="M14 6 V2 H26 V6" fill="none" stroke="#fff" stroke-width="3"/><rect x="0" y="6" width="40" height="30" rx="3" fill="#fff"/><rect x="0" y="17" width="40" height="2" fill="#2b5d9a"/><rect x="17" y="15" width="6" height="6" fill="#2b5d9a"/></svg></div>
  <h3 style="top:93px">Solid</h3>
  <p style="top:120px">Lorem Ipsum is simply dummy text of the printing and typesetting industry. Lorem Ipsum has been the industry's standard dummy text ever since the 1500s, when an unknown printer</p>
</div>

<h2 class="heading abs" style="left:133px">WELCOME TO HOLLIN &amp; CO</h2>
<div class="photo abs" style="left:133px;top:728px;width:300px;height:143px" role="img" aria-label="Two colleagues reviewing work on a laptop in a bright office"></div>
<p class="body-copy abs" style="top:890px">Sed ut perspiciatis unde omnis iste natus error sit voluptatem accusantium oremque laudantium, totam rem aperiam, eaque ipsa quae ab illo inventore veritatis et quasi architecto beatae vitae dicta sunt explicabo. Nemo enim ipsam voluptatem quia voluptas sit aspernatur aut odit aut fugit, sed quia consequuntur magni dolores eos qui ratione voluptatem sequi nesciunt.</p>
<p class="body-copy abs" style="top:976px">Neque porro quisquam est, qui dolorem ipsum quia dolor sit amet, consectetur, adipisci velit, sed quia non numquam eius modi tempora incidunt ut labore et dolore magnam aliquam quaerat voluptatem. Ut enim ad minima veniam, quis nostrum exercitationem ullam corporis suscipit laboriosam</p>

<h2 class="heading abs" style="left:452px">LATEST NEWS</h2>
<div class="pager abs" style="left:660px"><svg width="7" height="9"><path d="M6 1 L2 4.5 L6 8" fill="none" stroke="#fff" stroke-width="1.8"/></svg></div>
<div class="pager abs" style="left:685px"><svg width="7" height="9"><path d="M1 1 L5 4.5 L1 8" fill="none" stroke="#fff" stroke-width="1.8"/></svg></div>

<div class="news-img news-a abs" style="top:728px" role="img" aria-label="Financial reports with a calculator and a pen"></div>
<div class="date abs" style="top:824px">Sep<small>2014</small></div>
<p class="news-text abs" style="top:826px">Sed ut perspiciatis unde omnis iste natus error sit voluptatem accusantium doloremque laudantium, totam rem aperiam, eaque ipsa quae ... Read More</p>

<div class="news-img news-b abs" style="top:891px" role="img" aria-label="Businessman touching a glowing growth chart"></div>
<div class="date abs" style="top:987px">Sep<small>2014</small></div>
<p class="news-text abs" style="top:989px">Sed ut perspiciatis unde omnis iste natus error sit voluptatem accusantium doloremque laudantium, totam rem aperiam, eaque ipsa quae ... Read More</p>

<section class="partners abs">
  <span class="partner"><i></i>Calder Trust</span>
  <span class="partner">Pinefold</span>
  <span class="partner">Marrowby</span>
  <span class="partner">Oakhurst</span>
  <span class="partner">Lindqvist</span>
</section>

<footer class="site-footer abs">
  <div class="foot-nav abs"><span>Home</span><b>|</b><span>About</span><b>|</b><span>Services</span><b>|</b><span>Press</span><b>|</b><span>Career</span><b>|</b><span>Contact Us</span></div>
  <div class="copyright abs">© 2014 Company Name,All Rights Reserved</div>
  <div class="social abs"><span></span><span></span><span></span></div>
</footer>

</body>
</html>
```